Automotive Accessories Business Card

Design a business template that match our new logo design and our industry.

https://www.kelvorauto.com/

Target Market(s)

Aftermarket auto parts and accessories

Industry/Entity Type

automotive

Contact Information for Business Card

company logo

Font styles to use
Serif
Sans Serif

Colors
EB3D1F
EC4F4E
F09395
F8D3D4
FCEDEE

```html
<!DOCTYPE html>
<html lang="en">
<head>
<meta charset="utf-8">
<title>Kelvor Auto — Business Card</title>
<link rel="stylesheet" href="https://fonts.googleapis.com/css2?family=Montserrat:wght@500;600;800&family=Oswald:wght@600&display=swap">
<style>
  :root {
    --red: #EB3D1F;
    --red-soft: #EC4F4E;
    --pink: #F09395;
    --blush: #F8D3D4;
    --ink: #141414;
    --graphite: #3a3a3a;
    --paper-light: #f4f4f4;
    --paper-mid: #d9d9d9;
    --stage: #3f3237;
  }
  * { margin: 0; padding: 0; box-sizing: border-box; }
  html, body { width: 1200px; height: 840px; overflow: hidden; }
  body {
    background: var(--stage);
    font-family: "Montserrat", sans-serif;
    display: flex;
    flex-direction: column;
    align-items: center;
    justify-content: center;
    gap: 40px;
  }
  .card {
    position: relative;
    width: 640px;
    height: 366px;
    overflow: hidden;
    background: linear-gradient(120deg, var(--paper-light) 0%, var(--paper-mid) 100%);
    box-shadow: 0 10px 30px rgba(0,0,0,.35);
  }
  .card-shapes { position: absolute; inset: 0; }

  /* contact side */
  .brand-small {
    position: absolute; left: 40px; top: 120px;
    display: flex; align-items: center; gap: 10px;
  }
  .brand-mark { width: 14px; height: 14px; background: var(--red); }
  .brand-name {
    font-weight: 800; font-size: 26px; letter-spacing: 1px;
    color: var(--graphite);
  }
  .car-art {
    position: absolute; left: 110px; top: 205px; width: 360px; height: 140px;
    border-radius: 60px 90px 30px 30px;
    background: linear-gradient(100deg, #b3130f 0%, var(--red) 55%, var(--red-soft) 100%);
  }
  .contact-title {
    position: absolute; left: 370px; top: 36px;
    font-family: "Oswald", sans-serif; font-weight: 600;
    font-size: 22px; letter-spacing: 1px; color: #fff;
  }
  .contact-arrows { position: absolute; left: 548px; top: 40px; }
  .contact-list {
    position: absolute; left: 384px; top: 92px;
    list-style: none; display: flex; flex-direction: column; gap: 9px;
  }
  .contact-item {
    display: flex; align-items: flex-start; gap: 10px;
    font-size: 12.5px; font-weight: 500; line-height: 1.35; color: var(--ink);
  }
  .contact-icon {
    flex: none; width: 20px; height: 20px; border-radius: 50%;
    background: var(--red); display: flex; align-items: center; justify-content: center;
  }

  /* logo side */
  .tread-band {
    position: absolute; left: 0; width: 100%; height: 58px;
    background: linear-gradient(90deg, var(--paper-light), #ececec 50%, var(--paper-light));
  }
  .tread-band.top { top: 28px; }
  .tread-band.bottom { bottom: 28px; }
  .brand-large {
    position: absolute; inset: 0;
    display: flex; align-items: center; justify-content: center; gap: 18px;
  }
  .brand-large .brand-mark { width: 30px; height: 30px; }
  .brand-large .brand-name { font-size: 56px; letter-spacing: 3px; }
</style>
</head>
<body>

  <section class="card card-contact">
    <svg class="card-shapes" viewBox="0 0 640 366" width="640" height="366" aria-hidden="true">
      <polygon points="0,300 640,250 640,366 0,366" fill="var(--ink)"/>
      <polygon points="0,270 260,250 260,262 0,286" fill="#ffffff"/>
      <polygon points="640,118 640,252 400,272" fill="var(--red)"/>
      <polygon points="352,40 600,30 612,62 360,76" fill="var(--red)"/>
    </svg>

    <div class="brand-small">
      <span class="brand-mark"></span>
      <span class="brand-name">KELVOR AUTO</span>
    </div>

    <div class="car-art" role="img" aria-label="Illustration of a red sports car"></div>

    <h2 class="contact-title">CONTACT US</h2>
    <svg class="contact-arrows" width="44" height="26" viewBox="0 0 44 26" aria-hidden="true">
      <path d="M4 5 L14 13 L4 21 M16 5 L26 13 L16 21 M28 5 L38 13 L28 21" stroke="#fff" stroke-width="3" fill="none"/>
    </svg>

    <ul class="contact-list">
      <li class="contact-item">
        <span class="contact-icon"><svg width="10" height="10" viewBox="0 0 10 10"><rect x="2.5" y="0.5" width="5" height="9" rx="1" fill="#fff"/></svg></span>
        1-800-555-0142
      </li>
      <li class="contact-item">
        <span class="contact-icon"><svg width="11" height="9" viewBox="0 0 11 9"><rect x="0.5" y="0.5" width="10" height="8" fill="none" stroke="#fff"/><path d="M0.5 0.5 L5.5 5 L10.5 0.5" fill="none" stroke="#fff"/></svg></span>
        sales@kelvorauto.com
      </li>
      <li class="contact-item">
        <span class="contact-icon"><svg width="11" height="11" viewBox="0 0 11 11"><circle cx="5.5" cy="5.5" r="4.5" fill="none" stroke="#fff"/><path d="M1 5.5 H10 M5.5 1 V10" stroke="#fff"/></svg></span>
        www.kelvorauto.com
      </li>
      <li class="contact-item">
        <span class="contact-icon"><svg width="9" height="11" viewBox="0 0 9 11"><path d="M4.5 10.5 C1 6 0.5 4.5 0.5 4 A4 4 0 0 1 8.5 4 C8.5 4.5 8 6 4.5 10.5Z" fill="#fff"/><circle cx="4.5" cy="4" r="1.4" fill="var(--red)"/></svg></span>
        <span>240 W. Harbor Ave. Unit B<br>Riverside, CA 92501<br>United States</span>
      </li>
    </ul>
  </section>

  <section class="card card-logo">
    <div class="tread-band top" role="img" aria-label="Faint tyre-tread chevron pattern"></div>
    <div class="tread-band bottom" role="img" aria-label="Faint tyre-tread chevron pattern"></div>
    <div class="brand-large">
      <span class="brand-mark"></span>
      <span class="brand-name">KELVOR AUTO</span>
    </div>
  </section>

</body>
</html>
```